Mushroom Packaging - will require space for UPC code and other disclosures.

We are seeking to make packaging labels for our mushrooms.

Target Market(s)

Retail packaging label - there will be 20 different labels. We wish assistance on many different iterations changing the words and colors to differentiat new products

Industry/Entity Type

Retail mushroom packaging

Logo Text

Brand name is Meadow and Plate - space for label specifics as shown in examples

Logo styles of interest
Pictorial/Combination Logo
Requirements
Must have
• Must be a 2 inch by 3 inch label and must say product of USA, keep refridgerated, Make the name of the products most important part
Nice to have
• Ability to work with deisgner after the project is complete.
Should not have
• small fonts for the type of product. Please start with Sliced Shiitake Mushrooms Later we will add varations for other types such as Crimini Portabella Shiitake Oyster King Trumpets

```html
<!DOCTYPE html>
<html lang="en">
<head>
<meta charset="utf-8">
<title>Meadow and Plate – Sliced Shiitake Mushrooms Label</title>
<link rel="stylesheet" href="https://fonts.googleapis.com/css2?family=Open+Sans:wght@600;700&family=Roboto+Condensed:wght@400;500&family=Anton&display=swap">
<style>
  :root {
    --canvas: #ffffff;
    --rim: #000000;
    --gold: #fbbd55;
    --field: #0f9443;
    --badge: #f4874b;
    --ink-light: #ffffff;
    --ink-dark: #111111;
  }
  html, body {
    margin: 0;
    padding: 0;
    width: 1200px;
    height: 900px;
    overflow: hidden;
    background: var(--canvas);
  }
  .label {
    position: relative;
    width: 1200px;
    height: 900px;
  }
  .label-shape {
    position: absolute;
    inset: 0;
  }
  .brand-badge {
    position: absolute;
    left: 455px;
    top: 186px;
    width: 290px;
    height: 110px;
  }
  .brand-name {
    position: absolute;
    left: 455px;
    top: 222px;
    width: 290px;
    text-align: center;
    font-family: "Roboto Condensed", sans-serif;
    font-weight: 500;
    font-size: 25px;
    letter-spacing: 0.5px;
    color: var(--ink-dark);
    margin: 0;
  }
  .variant-flag {
    position: absolute;
    left: 180px;
    top: 288px;
    width: 190px;
    height: 125px;
  }
  .variant-name {
    position: absolute;
    left: 200px;
    top: 312px;
    width: 150px;
    text-align: center;
    font-family: "Anton", sans-serif;
    font-size: 40px;
    line-height: 1;
    color: var(--ink-dark);
    transform: rotate(-6deg);
    margin: 0;
  }
  .product-name {
    position: absolute;
    left: 0;
    top: 318px;
    width: 1200px;
    margin: 0;
    font-family: "Open Sans", sans-serif;
    font-weight: 700;
    font-size: 128px;
    line-height: 108px;
    color: var(--ink-light);
    text-align: center;
    letter-spacing: -1px;
  }
  .product-name .line-top {
    display: block;
    padding-left: 0;
    margin-left: 0;
    transform: translateX(0);
  }
  .disclosures {
    position: absolute;
    left: 300px;
    top: 554px;
    margin: 0;
    font-family: "Roboto Condensed", sans-serif;
    color: var(--ink-light);
    font-size: 20px;
    line-height: 27px;
  }
  .disclosures .net-weight {
    display: block;
    margin-top: 6px;
    padding-left: 68px;
    font-size: 25px;
  }
  .weight-box {
    position: absolute;
    left: 593px;
    top: 551px;
    width: 232px;
    height: 95px;
    background: var(--ink-light);
  }
  .website {
    position: absolute;
    left: 0;
    top: 665px;
    width: 1200px;
    text-align: center;
    margin: 0;
    font-family: "Open Sans", sans-serif;
    font-weight: 600;
    font-size: 20px;
    color: var(--ink-light);
  }
</style>
</head>
<body>
<main class="label">
  <svg class="label-shape" width="1200" height="900" viewBox="0 0 1200 900" aria-hidden="true">
    <ellipse cx="600" cy="462" rx="452" ry="288" fill="var(--rim)"/>
    <ellipse cx="600" cy="462" rx="418" ry="270" fill="var(--gold)"/>
    <ellipse cx="600" cy="462" rx="410" ry="262" fill="var(--field)"/>
  </svg>

  <svg class="brand-badge" viewBox="0 0 290 110" aria-hidden="true">
    <ellipse cx="145" cy="55" rx="143" ry="53" fill="var(--badge)" stroke="var(--rim)" stroke-width="2"/>
  </svg>
  <p class="brand-name">MEADOW AND PLATE</p>

  <svg class="variant-flag" viewBox="0 0 190 125" aria-hidden="true">
    <path d="M6 44 Q60 40 95 28 Q140 14 178 8 L184 84 Q140 88 100 100 Q60 112 14 116 Z"
          fill="var(--gold)" stroke="var(--rim)" stroke-width="1.5"/>
  </svg>
  <p class="variant-name">SLICED</p>

  <h1 class="product-name">
    <span class="line-top">&nbsp;&nbsp;Shiitake</span>
    <span class="line-bottom">Mushrooms</span>
  </h1>

  <p class="disclosures">
    PRODUCT OF USA<br>
    Keep Refridgerated
    <span class="net-weight">NET WT.</span>
  </p>
  <div class="weight-box"></div>

  <p class="website">www.meadow-plate.com</p>
</main>
</body>
</html>
```